Brochure design for Veltrisa

Create a bi-fold A5 size brochure. I have attached our logo and the written content to be included in the brochure. So the brochure will have a total of 4 pages (front page, inner two pages, back page). End source files need to include final printable brochure as well as editable files.

```html
<!DOCTYPE html>
<html lang="en">
<head>
<meta charset="utf-8">
<title>Veltrisa Brochure – Back Page</title>
<link rel="stylesheet" href="https://fonts.googleapis.com/css2?family=Sora:wght@400;700&display=swap">
<style>
  :root {
    --bg: #ffffff;
    --page: #ffffff;
    --ink: #1c1c1c;
    --heading: #1467ad;
    --rule: #4aa53c;
    --band-blue: #0568b0;
    --band-teal: #4a9a9a;
    --band-green: #8fc33f;
    --band-text: #ffffff;
  }
  * { margin: 0; padding: 0; box-sizing: border-box; }
  html, body { width: 1200px; height: 1200px; overflow: hidden; background: var(--bg); }
  body { font-family: "Sora", sans-serif; color: var(--ink); position: relative; }

  .page {
    position: absolute; left: 196px; top: 30px; width: 789px; height: 1120px;
    background: var(--page);
  }
  .section { position: absolute; left: 68px; width: 654px; }
  .section-title {
    font-size: 25px; font-weight: 700; color: var(--heading);
    line-height: 32px; padding-bottom: 1px;
    border-bottom: 2px solid var(--rule);
  }
  .section-body {
    margin: 15px 0 0 21px;
    font-size: 16.6px; line-height: 22.6px; letter-spacing: -0.1px;
    white-space: nowrap;
  }
  .drugs { top: 63px; }
  .diet { top: 391px; }
  .descent { top: 629px; }

  .contact-band {
    position: absolute; left: 0; bottom: 0; width: 100%; height: 238px;
    background: linear-gradient(90deg, var(--band-blue) 0%, var(--band-teal) 50%, var(--band-green) 100%);
    color: var(--band-text);
    padding: 30px 0 0 68px;
    font-size: 16.6px; line-height: 22.6px;
  }
  .contact-band p { margin-bottom: 16px; white-space: nowrap; }
</style>
</head>
<body>
  <main class="page">
    <section class="section drugs">
      <h2 class="section-title">DNA &amp; Drugs</h2>
      <p class="section-body">
        Scientific research has shown that the response rate for many prescribed<br>
        drugs is as low as 50% and that genetic factors can account for up to 95%<br>
        of drug-response variability and susceptibility.2-3 In other words, many of<br>
        the drugs you take in your lifetime will likely be inadequately dosed, leading<br>
        to potential side effects or no effects at all. With VeltrisaTM, you and your<br>
        doctor can proactively identify appropriate types, and dosages, for a range<br>
        of prescribed and over-the-counter medications. This includes medications<br>
        you currently take and any commons future medications you are likely<br>
        to encounter at some stage in your life. A number of studies have shown<br>
        that over 74% of people taking a genetic test for medication compatibility<br>
        learned information that is relevant to them.4-7
      </p>
    </section>

    <section class="section diet">
      <h2 class="section-title">DNA &amp; Diet</h2>
      <p class="section-body">
        Certain foods are thought to inappropriately cause immune reactions in<br>
        genetically predisposed individuals. This can result in symptoms like fatigue,<br>
        bloating, bowel disturbances, headaches, migraines, joint aches, eczema<br>
        or acne8-11. DNA testing can help identify such foods as well as genes<br>
        associated with the metabolism and absorption of vitamins, minerals and<br>
        stimulants like coffee. The VeltrisaTM range of tests can even help create<br>
        precision diet and fitness plans based on your genes and goals.
      </p>
    </section>

    <section class="section descent">
      <h2 class="section-title">DNA &amp; Descent</h2>
      <p class="section-body">
        The discipline of genealogy has exploded over recent years with the ad-<br>
        vent of DNA testing. The VeltrisaTM range of tests can help you track and<br>
        understand your ancestry and paternity tests can help identify an individ-<br>
        ual’s biological father. Family planning tests can help identify a couple’s<br>
        risk profile for conceiving children with any of the dozens of known genetic<br>
        conditions that can affect humans.
      </p>
    </section>

    <footer class="contact-band">
      <p>For more information about VeltrisaTM or our products, please talk to your<br>local retailer or email us at enquiries@veltrisa.co</p>
      <p>Please note test availability may differ from region to region and is subject to<br>availability. Please talk to your local retailer for more information.</p>
      <p>For a list of approved VeltrisaTM retailers please visit www.veltrisa.co</p>
    </footer>
  </main>
</body>
</html>
```